Chartered accountants trying to make boring information more appealing!

We are UK based chartered accountants with various specialist areas of expertise. We need a template for a monthly mailer that we send to our clients and contacts to keep them updated with key financial news. The update is called Amber Reef and we'd like it to fit on one page of A4 that we can then drop text into. We would like it to be more appealing than just the usual calculators and audit papers associated with accountants. Our brand colours are blue and green.

Target Market(s)

Our clients range from small businesses to large pension fund trustees, charities and individuals. It must appeal to everyone.

Industry/Entity Type

Accounting

Colors
34a7d8
33b8a4
3277b5

Requirements
Must have
• Space for text. The title 'Amber Reef'. Our logo.
Nice to have
• Sky's the limit!
Should not have
• Shouldn't look homemade. I've attached an old one done in house - please avoid this!

```html
<!DOCTYPE html>
<html lang="en">
<head>
<meta charset="utf-8">
<title>Amber Reef – June 2016</title>
<link rel="stylesheet" href="https://fonts.googleapis.com/css2?family=Open+Sans:wght@400;600;700;800&display=swap">
<style>
  :root{
    --page-bg:#ece8e1;
    --paper:#ffffff;
    --navy:#3277b5;
    --sky:#34a7d8;
    --teal:#33b8a4;
    --blue-panel:#3f8ae6;
    --green-panel:#5ee898;
    --cyan-panel:#52d5ee;
    --band-grey:#e6e9ec;
    --ink:#2b2f36;
    --white:#ffffff;
  }
  *{box-sizing:border-box;margin:0;padding:0}
  html,body{width:1200px;height:1000px;overflow:hidden}
  body{background:var(--page-bg);font-family:"Open Sans",Arial,sans-serif;color:var(--ink)}
  .mailer{position:absolute;left:260px;top:20px;width:680px;height:960px;background:var(--paper);
    box-shadow:0 4px 18px rgba(0,0,0,.12);overflow:hidden}
  .header{position:absolute;left:0;top:0;width:680px;height:200px;
    background:linear-gradient(135deg,#eaf7fb 0%,#ffffff 55%,#f1f4f6 100%)}
  .title-tab{position:absolute;left:24px;top:62px;width:300px;height:58px;border-radius:0 16px 16px 0;
    background:linear-gradient(90deg,#8fd0f2,var(--sky) 40%,var(--navy));
    color:var(--white);font-weight:800;font-size:34px;letter-spacing:1px;line-height:58px;padding-left:22px;text-transform:uppercase}
  .issue-tab{position:absolute;left:60px;top:128px;width:230px;height:40px;
    background:linear-gradient(90deg,#4fe089,#8bf0b2);color:var(--white);font-weight:800;font-size:24px;line-height:40px;padding-left:30px}
  .logo-box{position:absolute;left:372px;top:18px;width:270px;height:68px;background:var(--white);
    border-left:5px solid var(--teal);border-right:5px solid var(--navy);display:flex;align-items:center;justify-content:center;gap:10px}
  .logo-box .mark{width:14px;height:14px;background:var(--navy)}
  .logo-box .name{font-size:30px;font-weight:600;color:var(--navy)}
  .strap{position:absolute;left:330px;top:104px;width:350px;height:78px;
    background:linear-gradient(90deg,var(--navy),var(--sky));clip-path:polygon(0 50%,28px 0,100% 0,100% 100%,28px 100%);
    color:var(--white);font-weight:700;font-size:17px;line-height:22px;text-align:center;padding:17px 10px 0 40px}
  .welcome{position:absolute;left:0;top:200px;width:680px;height:52px;background:var(--band-grey);
    font-weight:700;font-size:12.5px;line-height:17px;padding:9px 24px}
  .panel{position:absolute;color:var(--white);font-size:10.5px;line-height:15px;padding:16px 22px}
  .panel h2{font-size:15px;font-weight:700;margin-bottom:10px}
  .panel h3{font-size:12px;font-weight:700;margin:10px 0 6px}
  .panel p{margin-bottom:9px}
  .panel ul{list-style:none;margin-bottom:9px}
  .panel li::before{content:"▢ ";}
  .nlw{left:0;top:252px;width:340px;height:450px;background:linear-gradient(160deg,#4594ec,var(--navy))}
  .psa{left:340px;top:252px;width:340px;height:300px;background:var(--green-panel)}
  .psa-more{left:340px;top:552px;width:340px;height:150px;background:linear-gradient(135deg,#6ee0f3,var(--cyan-panel))}
  .pension{left:0;top:702px;width:680px;height:180px;background:var(--cyan-panel);padding-right:30px}
  .contact-strip{position:absolute;left:0;top:882px;width:680px;height:78px;background:var(--band-grey)}
  .contact-tab{position:absolute;left:0;top:16px;width:180px;height:46px;
    background:linear-gradient(90deg,var(--navy),var(--sky));clip-path:polygon(0 0,86% 0,100% 50%,86% 100%,0 100%);
    color:var(--white);font-weight:800;font-size:19px;line-height:46px;padding-left:20px;white-space:nowrap}
  .contact-list{position:absolute;left:192px;right:12px;top:27px;display:flex;justify-content:space-between;
    font-size:10px;font-weight:700;color:var(--navy);white-space:nowrap}
  .contact-list li{list-style:none;display:flex;align-items:center;gap:5px;flex-shrink:0}
  .contact-list svg{width:22px;height:22px;flex-shrink:0}
</style>
</head>
<body>
<main class="mailer">
  <header class="header">
    <div class="title-tab">Amber Reef</div>
    <div class="issue-tab">JUNE 2016</div>
    <div class="logo-box"><span class="mark"></span><span class="name">Hartwell</span></div>
    <div class="strap">Keeping you up to date<br>with the latest accounting news</div>
  </header>

  <div class="welcome">Welcome to Hartwell Amber Reef. This issue covers the new National Living Wage, PAYE Settlement Agreements and the latest news on pension contributions due to be announced in the Budget.</div>

  <section class="panel nlw">
    <h2>The new National Living Wage ("NLW")</h2>
    <p>From April 2016, the Government's new National Living Wage will become law. This means that all workers aged 25 and over are legally entitled to be paid at least £7.20 per hour.</p>
    <p>If you're an employer, you will need to make sure that you are paying your staff correctly from 1st April, as the National Living Wage will be enforced just as strongly as the current National Minimum Wage.</p>
    <p>To make sure that you are ready for the change, you must:</p>
    <ul>
      <li>Check which of your employees is eligible to receive the NLW</li>
      <li>Take the appropriate payroll actions</li>
      <li>Let your staff know about their new pay rates</li>
      <li>Check that your staff under 25 are earning at least the right rate of National Minimum Wage</li>
    </ul>
    <p>If you're concerned about the effects of the new National Living Wage or would like some help to implement the changes, why not call one of our Payroll experts on 0123 456 7890 for some specialist advice?</p>
    <p>You can find out more about the National Living Wage, including new rates of pay on the Government website at www.example.gov/wage-rates</p>
  </section>

  <section class="panel psa">
    <h2>PAYE Settlement Agreements ("PSA")</h2>
    <p>A PSA allows an employer to make one annual payment to cover all the tax and National Insurance due on small or irregular taxable benefits or expenses. This can be beneficial as it avoids the need to include these on annual P11D forms, or to calculate and charge tax and National Insurance on such items through the payroll.</p>
    <h3>What is covered?</h3>
    <p>A PSA is intended to cover items that are minor, irregular or impracticable, such as small gifts, occasional staff entertaining or a one-off relocation expense. It can also include items where it would be difficult to place a value on each employee's share of the benefit.</p>
  </section>

  <section class="panel psa-more">
    <p>A PSA cannot be used for items such as bonuses, round sum allowances, beneficial loans or more significant benefits such as company cars.</p>
    <p>If you apply after the start of the tax year, there are some restrictions on what you can include.</p>
  </section>

  <section class="panel pension">
    <h2>Pension Contributions</h2>
    <p>Gerald Osmond has dropped plans to end or alter tax relief on pension contributions.</p>
    <p>A proposed scheme would have scrapped upfront relief, worth an estimated £21bn to savers, but made pension pot withdrawals tax free. An alternative option was to set a flat rate of tax relief, which may have been unpopular with higher earners.</p>
    <p>Campaigners suggest that the Chancellor has missed a "huge opportunity" to tackle obvious pension inequality and help the lower paid, but others say he was right to protect existing reliefs and that radical reforms would have created new risks and imposed new administrative burdens on employers. Mr Osmond had been expected to unveil changes in the Budget on 16 March, but a Treasury source said it was "not the right time".</p>
  </section>

  <footer class="contact-strip">
    <div class="contact-tab">CONTACT US</div>
    <ul class="contact-list">
      <li><svg viewBox="0 0 24 24" aria-hidden="true"><circle cx="12" cy="12" r="11" fill="none" stroke="#3277b5" stroke-width="2"/><path d="M8 6.5l2 2-1.2 1.6c.8 1.8 2.2 3.2 4 4l1.6-1.2 2 2-1.4 1.6c-3.6-.4-7.6-4.4-8-8z" fill="#3277b5"/></svg>0123 456 7890</li>
      <li><svg viewBox="0 0 24 24" aria-hidden="true"><circle cx="12" cy="12" r="11" fill="none" stroke="#3277b5" stroke-width="2"/><rect x="6.5" y="8" width="11" height="8" fill="none" stroke="#3277b5" stroke-width="1.5"/><path d="M6.5 8l5.5 4.5L17.5 8" fill="none" stroke="#3277b5" stroke-width="1.5"/></svg>ANNA@HARTWELL.EXAMPLE</li>
      <li><svg viewBox="0 0 24 24" aria-hidden="true"><circle cx="12" cy="12" r="11" fill="none" stroke="#3277b5" stroke-width="2"/><circle cx="12" cy="12" r="6" fill="none" stroke="#3277b5" stroke-width="1.4"/><ellipse cx="12" cy="12" rx="2.6" ry="6" fill="none" stroke="#3277b5" stroke-width="1.2"/><path d="M6 12h12" stroke="#3277b5" stroke-width="1.2"/></svg>WWW.HARTWELL.EXAMPLE</li>
    </ul>
  </footer>
</main>
</body>
</html>
```